To design the Curriculum Vitae of a General Manager Legal

the objective is to redesign the attached Résumé for a senior level Internal Legal Executive in order to make it attractive, easily readable, catchy, modern looking while staying classy, elegant, sobre, and serious.
The résumé is attached to this project. it contains the followings sections : Photo; Contact Details; Summary; Education; Experience; Other.
Feel free to use photoshop to improve photo.
Updates

Target Market(s)

Legal community; law firms; Big corporations requiring internal legal senior executive

Font styles to use
Serif

Colors
ffffff
85cae6
33a6d7
0292cd
86cfc6
cfeae6
757575
919191
d9d9d9

Requirements
Must have
• classy; serious; professional; elegant; easy to read; catchy; modern;

```html
<!DOCTYPE html>
<html lang="en">
<head>
<meta charset="utf-8">
<title>Resume – Lina Haddad Morel</title>
<link href="https://fonts.googleapis.com/css2?family=Open+Sans:wght@300;400&family=Encode+Sans+Condensed:wght@500&family=Caladea:wght@400&display=swap" rel="stylesheet">
<style>
  :root {
    --paper: #ffffff;
    --title-tint: #cfe6e3;
    --band: #cfeae6;
    --band-label: #5f8583;
    --name: #757575;
    --contact: #4c6f6d;
    --heading: #4f7573;
    --body: #1e1e1e;
    --photo-dark: #3a2f2a;
    --photo-light: #b99680;
  }
  * { margin: 0; padding: 0; box-sizing: border-box; }
  html, body { width: 848px; height: 1200px; overflow: hidden; background: var(--paper); }
  .page { position: relative; width: 848px; height: 1200px; background: var(--paper); }

  .title {
    position: absolute; left: 67px; top: 32px;
    font-family: "Open Sans", sans-serif; font-weight: 300;
    font-size: 108px; line-height: 1; white-space: nowrap;
    color: var(--title-tint);
    transform: scaleX(0.85); transform-origin: left top;
  }
  .name {
    position: absolute; left: 131px; top: 153px;
    font-family: "Open Sans", sans-serif; font-weight: 300;
    font-size: 31px; color: var(--name); line-height: 1.2; white-space: nowrap;
  }
  .contact {
    position: absolute; left: 130px; top: 210px;
    font-family: "Encode Sans Condensed", sans-serif; font-weight: 500;
    font-size: 14px; line-height: 21px; color: var(--contact);
  }
  .portrait {
    position: absolute; left: 623px; top: 38px; width: 164px; height: 202px;
    background: radial-gradient(ellipse at 50% 45%, var(--photo-light) 0%, #8a6a58 45%, var(--photo-dark) 100%);
  }

  .band { position: absolute; left: 129px; width: 42px; background: var(--band); }
  .band-label {
    position: absolute; left: 50%; top: 17px;
    transform-origin: left top; transform: rotate(90deg) translateY(-50%);
    font-family: "Open Sans", sans-serif; font-weight: 300;
    font-size: 22px; letter-spacing: 1px; color: var(--band-label);
    white-space: nowrap; line-height: 1;
  }
  .band-summary { top: 289px; height: 538px; }
  .band-education { top: 860px; height: 284px; }

  .body-text {
    position: absolute; left: 337px; width: 455px;
    font-family: "Caladea", serif; font-size: 15px; line-height: 21.3px;
    color: var(--body); text-align: justify;
  }
  .summary-para { text-indent: 21px; }
  .p1 { top: 284px; }
  .p2 { top: 509px; }
  .p3 { top: 697px; }
  .p4 { top: 799px; }

  .school {
    position: absolute; left: 244px; white-space: nowrap;
    font-family: "Open Sans", sans-serif; font-weight: 300;
    font-size: 21px; line-height: 28px; color: var(--heading);
  }
  .school-1 { top: 866px; }
  .school-2 { top: 1004px; }
  .school-3 { top: 1054px; }

  .degree::before {
    content: ""; position: absolute; left: -25px; top: 9px;
    width: 5px; height: 5px; border-radius: 50%; background: var(--body);
  }
  .degree-1 { top: 904px; }
  .degree-2 { top: 959px; }
  .degree-3 { top: 1094px; }
</style>
</head>
<body>
<div class="page">
  <div class="title">RESUME</div>
  <div class="name">Lina Haddad Morel</div>
  <div class="contact">
    <div>mobile : +971 50 000 1234</div>
    <div>e-mail : lina.haddad@mailbox.com</div>
  </div>
  <div class="portrait" role="img" aria-label="Portrait photograph of the candidate"></div>

  <div class="band band-summary"><span class="band-label">SUMMARY</span></div>
  <p class="body-text summary-para p1">A senior qualified legal professional with more than 15 years of experience in private practice and in-house focusing on the following industries: Real Estate, Retail and Services, obtained in UAE, France and Syria. Practice transactional skills (M&amp;A, real estate, commercial, corporate restructuring, strategic funding), organizational skills (policies and procedures and authority matrix covering different contexts in corporate environment), lawyering skills (preemptive legal advice, and a multi jurisdiction litigation management expertise), managerial skills (enhancing the value add of the legal department as both a service provider and a risk gatekeeper).</p>
  <p class="body-text summary-para p2">Joined Noor Al Sahel Group in November 2011, an internationally recognized industry Leader in shopping malls, communities, retail and leisure across the Middle East, Africa and Asia, first as Legal Counsel at Noor Al Sahel Properties responsible for UAE Shopping Malls, Project management and communities, and then moved in Mai 2015 to Noor Al Sahel Retail - Marketline where currently I occupy the role of GM-Legal, focusing mainly on leading and managing the legal, compliance and risk management strategies across a wide geographic area of countries.</p>
  <p class="body-text summary-para p3">Prior to moving to Dubai, I have lived in Paris France, where I have worked in various organizations including the Global Court of Arbitration, a billing software company and a consultancy practice. I graduated from University of Lutetia Campus II with two Master Degrees.</p>
  <p class="body-text summary-para p4">Mother of Three, I am passionate about Bon Fide work towards Women Empowerment and Refugee Children Education.</p>

  <div class="band band-education"><span class="band-label">EDUCATION</span></div>
  <div class="school school-1">University of Lutetia (Campus II) Paris – France</div>
  <div class="body-text degree degree-1">Master degree in Litigation, Arbitration, and Alternative Dispute Resolution (98- 99)</div>
  <div class="body-text degree degree-2">Master degree in commercial law (97-98)</div>
  <div class="school school-2">Institute of Comparative Studies Paris - France (97-98)</div>
  <div class="school school-3">University of the Levant – Syria</div>
  <div class="body-text degree degree-3">Law degree (92-96)</div>
</div>
</body>
</html>
```